International horse riding portal needs web design

We are looking for the web design for the new "Vosmerik" web portal.

Offers from the world of horses and riding should be found on this portal, eg from the categories riding schools, riding holidays, farriers, riding stables, riding stables. And all information about riding.

It is important that the different areas can be found easily and clearly. For some categories, some features should already be available in the search bar.

In addition, the design should make you want to go horse riding. The user should be emotionally picked up on the landing page.

In the lower area, some offers should be advertised, eg from the areas of riding holidays, riding training, and horse trading.

Please use the colors from the logo for the design.
C100 M50 Y10 K50 and C0 M20 Y60 K30

```html
<!DOCTYPE html>
<html lang="en">
<head>
<meta charset="utf-8">
<title>Vosmerik – Horse Riding Portal</title>
<link href="https://fonts.googleapis.com/css2?family=Cinzel:wght@400;600;700&family=Nunito+Sans:wght@400;600;700;800&display=swap" rel="stylesheet">
<style>
:root{
  --navy:#0b3d6b;
  --navy-dark:#083257;
  --gold:#b08d4f;
  --gold-light:#c9a96a;
  --text:#3d3d3d;
  --muted:#6b6b6b;
  --line:#d9d9d9;
  --paper:#f6f4f1;
  --white:#fff;
}
*{box-sizing:border-box;margin:0;padding:0}
html,body{width:1200px;height:3395px;overflow:hidden}
body{position:relative;font-family:"Nunito Sans",sans-serif;color:var(--text);background:var(--white)}
.abs{position:absolute}
.serif{font-family:"Cinzel",serif}
.gold-btn{position:absolute;display:flex;align-items:center;justify-content:center;background:linear-gradient(90deg,#a8844a,#c9a96a,#a8844a);color:#fff;font-weight:800;border-radius:40px;letter-spacing:.3px}

/* header */
.site-header{position:absolute;left:0;top:0;width:1200px;height:108px;background:#fff;box-shadow:0 2px 6px rgba(0,0,0,.08);z-index:3}
.brand{left:119px;top:30px;width:140px;text-align:center}
.brand-mark{display:block;width:26px;height:26px;margin:0 auto 6px;border-radius:50%;background:var(--gold)}
.brand-name{font-family:"Cinzel",serif;font-weight:700;font-size:26px;color:var(--navy)}
.search{left:349px;top:13px;width:350px;height:36px;border:1px solid #bbb;border-radius:20px;font-size:11px;color:#888;padding:11px 20px}
.search-btn{position:absolute;right:2px;top:2px;width:30px;height:30px;border-radius:50%;background:var(--gold)}
.top-links{top:21px;font-size:13px;font-weight:700;color:#222}
.login{left:992px;top:13px;width:85px;height:32px;background:var(--gold);color:#fff;font-size:13px;font-weight:700;display:flex;align-items:center;justify-content:center}
.main-nav{top:68px;font-size:16px;color:#222;font-weight:600}
.main-nav span::after{content:"";display:inline-block;width:6px;height:6px;border-right:2px solid #333;border-bottom:2px solid #333;transform:rotate(45deg);margin-left:6px;position:relative;top:-3px}
.main-nav span.plain::after{display:none}

/* hero */
.hero{left:0;top:108px;width:1200px;height:545px;background:radial-gradient(ellipse at 20% 20%,#f3b64c 0%,#c9791f 30%,#7b4a1c 65%,#3b2412 100%)}
.hero-title{left:103px;top:222px;color:#fff}
.hero-title .small{font-family:"Cinzel",serif;font-size:34px;letter-spacing:1px}
.hero-title .big{font-family:"Cinzel",serif;font-size:68px;font-weight:600;line-height:70px}
.hero-title p{font-size:14px;line-height:21px;margin-left:9px;margin-top:4px}
.tab{top:464px;height:42px;border-radius:8px 8px 0 0;background:#e8ddd0;color:var(--navy);font-weight:800;font-size:15px;display:flex;align-items:center;justify-content:center}
.tab.active{background:#fff}
.finder{left:109px;top:506px;width:889px;height:83px;background:#fff;border-radius:0 10px 10px 10px;box-shadow:0 4px 14px rgba(0,0,0,.15)}
.radio{top:37px;font-size:14px;color:var(--navy);display:flex;align-items:center}
.radio i{width:14px;height:14px;border:1.5px solid var(--navy);border-radius:50%;margin-right:6px;position:relative}
.radio i.on::after{content:"";position:absolute;left:2.5px;top:2.5px;width:6px;height:6px;border-radius:50%;background:var(--navy)}
.zip{left:578px;top:21px;width:216px;height:36px;border:1px solid #ccc;font-size:12px;color:#888;padding:10px 28px}
.find{left:794px;top:21px;width:77px;height:36px;background:var(--navy);color:#fff;font-weight:800;font-size:14px;display:flex;align-items:center;justify-content:center}

/* intro */
.intro-title{left:150px;top:663px;width:900px;text-align:center;font-family:"Cinzel",serif;font-size:29px;color:var(--navy);line-height:37px;letter-spacing:.5px}
.rule{height:3px;background:var(--gold)}
.intro-text{left:280px;top:778px;width:640px;text-align:center;font-size:15px;line-height:24px;color:var(--text)}
.intro-text p+p{margin-top:10px}

/* categories */
.cat{top:994px;width:219px;height:211px;background:#fff;border:1px solid var(--line)}
.cat .ph{height:166px}
.cat .lbl{height:45px;display:flex;align-items:center;justify-content:center;font-weight:800;font-size:16px;color:var(--navy);letter-spacing:.3px}
.cat.active{top:976px;height:234px;background:var(--navy);border-color:var(--navy)}
.cat.active .ph{height:184px}
.cat.active .lbl{color:#fff;height:50px}
.circle-arrow{width:58px;height:58px;border-radius:50%;background:var(--navy)}

/* offers */
.offers{left:0;top:1290px;width:1200px;height:620px;background:linear-gradient(180deg,#efece7,#f3f0ea 60%,#ece8e0)}
.sec-title{font-family:"Cinzel",serif;font-size:34px;color:var(--navy);letter-spacing:.5px}
.sec-title em{font-style:normal;color:var(--gold)}
.offer{top:1427px;width:308px;height:403px;background:#fff;border:1px solid #ddd;text-align:center}
.offer .ph{height:216px}
.offer h3{font-size:18px;font-weight:800;color:var(--navy);line-height:21px;margin-top:26px}
.offer p{font-size:13px;color:var(--muted);line-height:20px;margin-top:12px}
.offer.active{border-bottom:4px solid var(--gold)}
.soft-arrow{width:44px;height:44px;border-radius:50%;background:rgba(255,255,255,.7)}

/* training */
.training-title{left:115px;top:2035px}
.training-text{left:117px;top:2118px;width:420px;font-size:17px;line-height:29px;color:var(--text)}
.training-text p+p{margin-top:5px}

/* horses */
.horses{left:0;top:2475px;width:1200px;height:520px;background:var(--paper)}
.horse-card{background:#fff}
.round{width:56px;height:56px;border-radius:50%;background:#e6e3df}

/* footer */
.footer{left:0;top:2935px;width:1200px;height:460px}
.f-head{font-family:"Cinzel",serif;font-weight:700;font-size:15px;color:#fff;letter-spacing:.3px}
.f-rule{width:40px;height:2px;background:#fff;margin-top:8px}
.f-links{font-size:12px;color:#fff;line-height:29px}
.f-contact{font-size:12px;color:#fff;line-height:20px}
</style>
</head>
<body>

<header class="site-header">
  <div class="abs brand"><span class="brand-mark"></span><span class="brand-name">VOSMERIK</span></div>
  <div class="abs search">Search &gt; Feature
    <span class="search-btn"><svg width="30" height="30" viewBox="0 0 30 30"><circle cx="14" cy="14" r="6" fill="none" stroke="#fff" stroke-width="2.2"/><line x1="18.5" y1="18.5" x2="22" y2="22" stroke="#fff" stroke-width="2.5" stroke-linecap="round"/></svg></span>
  </div>
  <div class="abs top-links" style="left:748px">News</div>
  <div class="abs top-links" style="left:819px">Resources</div>
  <div class="abs top-links" style="left:921px">My List</div>
  <div class="abs login">Login</div>
  <nav>
    <div class="abs main-nav" style="left:343px"><span>About Us</span></div>
    <div class="abs main-nav" style="left:464px"><span>Riding School</span></div>
    <div class="abs main-nav" style="left:611px"><span>Riding Holidays</span></div>
    <div class="abs main-nav" style="left:771px"><span>Farries</span></div>
    <div class="abs main-nav" style="left:868px"><span>Riding Stables</span></div>
    <div class="abs main-nav" style="left:1019px"><span class="plain">Contact</span></div>
  </nav>
</header>

<section>
  <div class="abs hero" role="img" aria-label="Rider gently stroking a dark brown horse in warm golden evening light"></div>
  <svg class="abs" style="left:0;top:600px" width="1200" height="60" viewBox="0 0 1200 60" preserveAspectRatio="none">
    <path d="M0 50 Q600 -20 1200 50 L1200 60 L0 60 Z" fill="#fff"/>
    <path d="M0 50 Q600 -20 1200 50" fill="none" stroke="#b08d4f" stroke-width="5"/>
  </svg>
  <div class="abs hero-title">
    <div class="small">WELCOME TO</div>
    <div class="big">VOSMERIK</div>
    <p>Lorem ipsum dolor sit amet, consectetur adipis<br>cing elit, sed do eiusmod tempor inc</p>
  </div>
  <div class="abs tab active" style="left:109px;width:161px">Riding School</div>
  <div class="abs tab" style="left:278px;width:157px">Riding Holidays</div>
  <div class="abs tab" style="left:443px;width:121px">Farries</div>
  <div class="abs tab" style="left:567px;width:161px">Riding Stables</div>
  <div class="abs finder">
    <div class="abs radio" style="left:32px"><i class="on"></i>Feature First</div>
    <div class="abs radio" style="left:154px"><i></i>Feature Second</div>
    <div class="abs radio" style="left:300px"><i></i>Feature Third</div>
    <div class="abs radio" style="left:434px"><i></i>Feature Fourth</div>
    <div class="abs zip"><svg class="abs" style="left:12px;top:10px" width="10" height="14" viewBox="0 0 10 14"><path d="M5 0C2.2 0 0 2.2 0 5c0 3.5 5 9 5 9s5-5.5 5-9c0-2.8-2.2-5-5-5zm0 7a2 2 0 110-4 2 2 0 010 4z" fill="#0b3d6b"/></svg>Zip Code/ City</div>
    <div class="abs find">FIND</div>
  </div>
</section>

<section>
  <h1 class="abs intro-title">IHIC TECTIO BLAB INCIENIS AUT HILIQUO QUISQUI<br>AEPRECTUR? URESEQUOD QUI DITIS</h1>
  <div class="abs rule" style="left:566px;top:749px;width:80px;height:2px"></div>
  <div class="abs intro-text">
    <p>Lorem ipsum dolor sit amet, consectetur adipiscing elit, sed do eiusmod tempor inci-didunt ut labore et dolore magna aliqua. Ut enim ad minim.Lorem ipsum dolor sit am-et.Lorem ipsum dolor sit amet, consectetur adipiscing.</p>
    <p>Lorem ipsum dolor sit amet, consectetur adipiscing elit, sed do eiusmod tempor inci-didunt ut labore et dolore magna aliqua. Ut enim ad minim.</p>
  </div>
</section>

<section>
  <div class="abs circle-arrow" style="left:-29px;top:1060px"><svg width="58" height="58" viewBox="0 0 58 58"><path d="M41 21l-8 8 8 8" fill="none" stroke="#fff" stroke-width="3"/></svg></div>
  <div class="abs circle-arrow" style="left:1171px;top:1062px"><svg width="58" height="58" viewBox="0 0 58 58"><path d="M17 21l8 8-8 8" fill="none" stroke="#fff" stroke-width="3"/></svg></div>
  <div class="abs cat" style="left:47px"><div class="ph" role="img" aria-label="Young rider leaning forward on a grey horse" style="background:linear-gradient(135deg,#9aa08c,#5c5f52)"></div><div class="lbl">RIDING SCHOOLS</div></div>
  <div class="abs cat active" style="left:269px"><div class="ph" role="img" aria-label="Group of riders on horseback at sunset" style="background:linear-gradient(135deg,#e7a77a,#7a4a3c)"></div><div class="lbl">RIDING HOLIDAYS</div></div>
  <div class="abs cat" style="left:491px"><div class="ph" role="img" aria-label="Rider on a chestnut horse in a green forest" style="background:linear-gradient(135deg,#3f6b2d,#a5763e)"></div><div class="lbl">RIDING FARRIERS</div></div>
  <div class="abs cat" style="left:712px"><div class="ph" role="img" aria-label="Row of horses looking out of stable boxes" style="background:linear-gradient(135deg,#5d6a70,#2e3438)"></div><div class="lbl">RIDING STABLES</div></div>
  <div class="abs cat" style="left:935px"><div class="ph" role="img" aria-label="Rider on a bay horse in an arena" style="background:linear-gradient(135deg,#b59a7a,#4a3a2c)"></div><div class="lbl">ABOUT RIDING</div></div>
</section>

<section>
  <div class="abs offers" role="img" aria-label="Faded background of horses in a meadow"></div>
  <h2 class="abs sec-title" style="left:0;width:1200px;text-align:center;top:1334px">IHIC TECTIO BLAB <em>INCIENIS AUT</em></h2>
  <svg class="abs" style="left:557px;top:1382px" width="76" height="16" viewBox="0 0 76 16"><line x1="0" y1="8" x2="26" y2="8" stroke="#0b3d6b" stroke-width="2"/><circle cx="38" cy="8" r="4" fill="#0b3d6b"/><line x1="50" y1="8" x2="76" y2="8" stroke="#0b3d6b" stroke-width="2"/></svg>
  <div class="abs soft-arrow" style="left:44px;top:1598px"><svg width="44" height="44" viewBox="0 0 44 44"><path d="M26 14l-8 8 8 8" fill="none" stroke="#0b3d6b" stroke-width="3"/></svg></div>
  <div class="abs soft-arrow" style="left:1098px;top:1598px"><svg width="44" height="44" viewBox="0 0 44 44"><path d="M18 14l8 8-8 8" fill="none" stroke="#0b3d6b" stroke-width="3"/></svg></div>

  <article class="abs offer active" style="left:117px">
    <div class="ph" role="img" aria-label="Instructor lunging a young rider on a chestnut pony" style="background:linear-gradient(180deg,#8fb0c8,#6f8f4a 55%,#c9bfae)"></div>
    <h3>Sed ut perspiciatis unde<br>omnis iste natus</h3>
    <p>Lorem ipsum dolor sit amet, consecte-<br>tur adipiscing elit, sed eiusmod</p>
    <div class="gold-btn" style="left:86px;top:343px;width:135px;height:34px;font-size:11px">LEARN MORE ›</div>
  </article>
  <article class="abs offer" style="left:442px">
    <div class="ph" role="img" aria-label="Rider cantering a brown horse through autumn woods" style="background:linear-gradient(180deg,#e8e2d2,#a07a4c)"></div>
    <h3>Sed ut perspiciatis unde<br>omnis iste natus</h3>
    <p>Lorem ipsum dolor sit amet, consecte-<br>tur adipiscing elit, sed eiusmod</p>
    <div class="gold-btn" style="left:86px;top:343px;width:135px;height:34px;font-size:11px">LEARN MORE ›</div>
  </article>
  <article class="abs offer" style="left:766px">
    <div class="ph" role="img" aria-label="Show jumper clearing a fence under blue sky" style="background:linear-gradient(180deg,#4f86c6,#a9c2d8 60%,#7a5a3c)"></div>
    <h3>Sed ut perspiciatis unde<br>omnis iste natus</h3>
    <p>Lorem ipsum dolor sit amet, consecte-<br>tur adipiscing elit, sed eiusmod</p>
    <div class="gold-btn" style="left:86px;top:343px;width:135px;height:34px;font-size:11px">LEARN MORE ›</div>
  </article>
</section>

<section>
  <svg class="abs" style="left:580px;top:1910px" width="620" height="565" viewBox="0 0 620 565" role="img" aria-label="Woman stroking a dark brown horse at golden hour">
    <defs><radialGradient id="trainGlow" cx="0.25" cy="0.3" r="0.9"><stop offset="0" stop-color="#e9b24c"/><stop offset="0.45" stop-color="#8a5a22"/><stop offset="1" stop-color="#3a2614"/></radialGradient></defs>
    <polygon points="143,0 620,0 620,565 143,565 0,279" fill="url(#trainGlow)"/>
  </svg>
  <h2 class="abs sec-title training-title">HORSE RIDING <em>TRAINING</em></h2>
  <svg class="abs" style="left:117px;top:2082px" width="76" height="16" viewBox="0 0 76 16"><line x1="0" y1="8" x2="26" y2="8" stroke="#0b3d6b" stroke-width="2"/><circle cx="38" cy="8" r="4" fill="#0b3d6b"/><line x1="50" y1="8" x2="76" y2="8" stroke="#0b3d6b" stroke-width="2"/></svg>
  <div class="abs training-text">
    <p>Lorem ipsum dolor sit amet, consectetur adipisc-ing elit, sed do eiusmod tempor incididunt ut labore et dolore magna aliqua.</p>
    <p>Ut enim ad minim veniam, quis nostrud exercita-tion ullamco laboris nisi ut aliquip ex ea commodo consequat minim veniam, quis nostrud exercita</p>
  </div>
  <div class="gold-btn" style="left:115px;top:2321px;width:171px;height:46px;font-size:15px">LEARN MORE ›</div>
</section>

<section>
  <div class="abs horses"></div>
  <div class="abs" style="left:117px;top:2611px;font-size:15px;color:var(--navy);font-weight:600">RIDING HORSES</div>
  <h2 class="abs sec-title" style="left:117px;top:2632px;font-size:36px"><em>OUR</em> HORSES</h2>
  <svg class="abs" style="left:119px;top:2672px" width="76" height="16" viewBox="0 0 76 16"><line x1="0" y1="8" x2="26" y2="8" stroke="#0b3d6b" stroke-width="2"/><circle cx="38" cy="8" r="4" fill="#0b3d6b"/><line x1="50" y1="8" x2="76" y2="8" stroke="#0b3d6b" stroke-width="2"/></svg>
  <p class="abs" style="left:118px;top:2702px;width:290px;font-size:16px;line-height:28px">Lorem ipsum dolor sit amet, consect-etur adipiscing elit, sed do eiusmod-Lorem ipsum dolor sit.</p>
  <div class="abs round" style="left:113px;top:2803px"><svg width="56" height="56" viewBox="0 0 56 56"><path d="M36 28H20m6-6l-6 6 6 6" fill="none" stroke="#333" stroke-width="2"/></svg></div>
  <div class="abs round" style="left:178px;top:2803px"><svg width="56" height="56" viewBox="0 0 56 56"><path d="M20 28h16m-6-6l6 6-6 6" fill="none" stroke="#333" stroke-width="2"/></svg></div>

  <div class="abs" role="img" aria-label="Chestnut horse with white blaze and flowing mane" style="left:456px;top:2591px;width:252px;height:264px;background:linear-gradient(135deg,#c9a46a,#8a4a22)"></div>
  <div class="abs" role="img" aria-label="Black horse standing in a field of red poppies" style="left:959px;top:2591px;width:241px;height:264px;background:linear-gradient(180deg,#7c8c84,#3a3a32 55%,#c4452c)"></div>
  <div class="abs horse-card" style="left:708px;top:2571px;width:251px;height:301px;box-shadow:0 6px 18px rgba(0,0,0,.25)">
    <div role="img" aria-label="Close-up of a bay horse wearing a bridle" style="height:301px;background:linear-gradient(180deg,#3a302c,#6e3d25 60%,#2a211c)"></div>
    <div class="abs" style="left:0;bottom:0;width:251px;height:58px;background:rgba(0,0,0,.55)"></div>
    <div class="abs" style="left:18px;bottom:17px;color:#fff;font-weight:800;font-size:17px">Horse Name</div>
    <div class="abs" style="left:155px;bottom:14px;color:#fff;font-size:9px;line-height:17px"><b>Birth Year:</b> 2018<br><b>Gender:</b> Gelding</div>
  </div>
</section>

<footer class="abs footer">
  <svg class="abs" style="left:0;top:0" width="1200" height="460" viewBox="0 0 1200 460" preserveAspectRatio="none">
    <path d="M0 8 Q600 55 1200 8 L1200 460 L0 460 Z" fill="#0b3d6b"/>
  </svg>
  <div class="abs" style="left:119px;top:120px;width:191px;text-align:center">
    <span style="display:block;width:60px;height:60px;margin:0 auto 12px;border-radius:50%;background:#fff"></span>
    <span style="font-family:'Cinzel',serif;font-weight:700;font-size:30px;color:#fff">VOSMERIK</span>
  </div>
  <div class="abs" style="left:359px;top:123px"><div class="f-head">NAVIGATION</div><div class="f-rule"></div>
    <div class="f-links" style="margin-top:6px">About Us<br>Riding School<br>Riding Holidays<br>Farries<br>Riding Stables</div></div>
  <div class="abs" style="left:546px;top:125px"><div class="f-head">CONTACT US</div><div class="f-rule"></div></div>
  <svg class="abs" style="left:549px;top:177px" width="16" height="22" viewBox="0 0 10 14"><path d="M5 0C2.2 0 0 2.2 0 5c0 3.5 5 9 5 9s5-5.5 5-9c0-2.8-2.2-5-5-5zm0 7a2 2 0 110-4 2 2 0 010 4z" fill="#fff"/></svg>
  <div class="abs f-contact" style="left:581px;top:173px">48 Meadowgate Lane P.O. Box 210<br>Elmsford, Ontario&nbsp; K7R 3P4</div>
  <svg class="abs" style="left:548px;top:220px" width="20" height="20" viewBox="0 0 24 24"><path d="M6.6 10.8a15 15 0 006.6 6.6l2.2-2.2a1 1 0 011-.25 11.4 11.4 0 003.6.57 1 1 0 011 1V20a1 1 0 01-1 1A17 17 0 013 4a1 1 0 011-1h3.5a1 1 0 011 1c0 1.25.2 2.45.57 3.57a1 1 0 01-.25 1z" fill="#fff"/></svg>
  <div class="abs f-contact" style="left:581px;top:221px;font-weight:700">Tel: (555) 204-8817</div>
  <svg class="abs" style="left:548px;top:254px" width="22" height="16" viewBox="0 0 22 16"><rect x="1" y="1" width="20" height="14" fill="none" stroke="#fff" stroke-width="2"/><path d="M1 1l10 8 10-8M1 15l7-6M21 15l-7-6" fill="none" stroke="#fff" stroke-width="1.6"/></svg>
  <div class="abs f-contact" style="left:581px;top:253px">Email: info@vosmerik.com</div>
  <div class="abs" style="left:840px;top:125px"><div class="f-head">FOLLOW US</div><div class="f-rule"></div></div>
  <div class="abs" style="left:840px;top:169px;width:208px;height:34px;background:#fff;font-size:10px;color:#777;padding:11px 14px">Your Email address</div>
  <div class="abs" style="left:840px;top:222px;width:208px;text-align:center;color:#fff;font-weight:800;font-size:12px">SUBSCRIBE</div>
  <span class="abs" aria-label="Social profile" style="left:842px;top:273px;width:22px;height:22px;border-radius:50%;background:#fff"></span>
  <span class="abs" aria-label="Social profile" style="left:880px;top:273px;width:22px;height:22px;border-radius:50%;background:#fff"></span>
  <span class="abs" aria-label="Social profile" style="left:918px;top:273px;width:22px;height:22px;border-radius:50%;background:#fff"></span>
  <div class="abs" style="left:0;top:398px;width:1200px;height:1px;background:rgba(255,255,255,.2)"></div>
  <div class="abs" style="left:0;top:414px;width:1200px;text-align:center;color:#fff;font-size:13px">Copyright © 2022 Vosmerik All Right Reserved</div>
</footer>

</body>
</html>
```